Create Print and Packaging Designs for premium tea range

We look for unique and eye catching design for our premium tea packaging. 6 types of tea, all the teas would have the same design with changes shown by colour and typography. (Purple, Blue, Green,Yellow, Orange and Red each tea would have one of these colours assigned to it)
We need to create a brand image, which is timeless, specialist, simple, elegant, colourful and represents good quality and taste.
- Brightly coloured maybe with two contrasting colours in one pack
- They can be in an unusual form, however, there should not be any problems with them fitting on a standard grocer’s shelf.
- We like the idea of die cut or pack with windows
- The openings should have a tamper evident label
- The packs are designed for easily packaged together in a carton ( for storage and delivery)
- Not too humorous
loose leaf or teabags would be vacuum packed with see-through plastic before packing in these cartons.size- 50g
We have uploaded a few designs that we liked and hope to be able to give you some ideas of what we are looking for.

```html
<!DOCTYPE html>
<html lang="en">
<head>
<meta charset="utf-8">
<title>Black Tea – Peach Apricot – Carton Front Panel</title>
<link rel="stylesheet" href="https://fonts.googleapis.com/css2?family=Courgette&family=Tinos:wght@400;700&display=swap">
<style>
  :root {
    --page-bg: #ffffff;
    --panel-cream: #fdf3ec;
    --warm-yellow: #f7c54a;
    --warm-orange: #ef9a3e;
    --blush: #f2b9a8;
    --title-ink: #1c1410;
    --flavour-red: #a0332a;
    --band-red: #7a1a1c;
    --band-red-dark: #4d0d10;
    --weight-red: #b3211d;
    --body-ink: #3a2e28;
    --brand-ink: #8a2a20;
    --splash-green: #a9c2ab;
    --fruit-orange: #f3b260;
    --band-text: #f6e7d7;
  }
  html, body {
    margin: 0;
    padding: 0;
    width: 1200px;
    height: 848px;
    overflow: hidden;
    background: var(--page-bg);
  }
  .carton-front {
    position: absolute;
    left: 40px;
    top: 144px;
    width: 1120px;
    height: 560px;
    overflow: hidden;
    background: linear-gradient(90deg, var(--warm-yellow) 0%, #fbe2a6 10%, var(--panel-cream) 24%, #fffaf5 55%, #fbe9df 78%, var(--blush) 88%, var(--warm-orange) 100%);
    box-shadow: 0 2px 6px rgba(0,0,0,0.18);
  }
  .leaf-texture {
    position: absolute;
    top: 0;
    height: 480px;
  }
  .leaf-texture--left {
    left: 0;
    width: 130px;
    background: linear-gradient(90deg, rgba(245,180,60,0.6), rgba(250,215,140,0));
  }
  .leaf-texture--right {
    right: 0;
    width: 240px;
    background: linear-gradient(90deg, rgba(244,170,150,0), rgba(232,120,70,0.6));
  }

  .side-title {
    position: absolute;
    left: 20px;
    top: 92px;
    margin: 0;
    font: 400 46px/1 "Courgette", cursive;
    color: var(--title-ink);
  }
  .side-flavour {
    position: absolute;
    left: 32px;
    top: 146px;
    margin: 0;
    font: 400 30px/1 "Tinos", serif;
    color: var(--flavour-red);
  }
  .side-copy {
    position: absolute;
    left: 22px;
    top: 196px;
    width: 200px;
    margin: 0;
    font: 400 15px/1.2 "Tinos", serif;
    color: var(--body-ink);
  }
  .side-disclaimer {
    position: absolute;
    left: 22px;
    top: 306px;
    width: 200px;
    margin: 0;
    font: 400 10px/1.3 "Tinos", serif;
    color: var(--body-ink);
  }
  .distributor {
    position: absolute;
    left: 22px;
    top: 412px;
    margin: 0;
    font: 700 13px/1.3 "Tinos", serif;
    color: var(--body-ink);
  }

  .tea-window {
    position: absolute;
    left: 252px;
    top: 14px;
    width: 256px;
    height: 430px;
    background: var(--splash-green);
  }

  .product-title {
    position: absolute;
    left: 548px;
    top: 40px;
    margin: 0;
    font: 400 86px/1 "Courgette", cursive;
    color: var(--title-ink);
  }
  .product-flavour {
    position: absolute;
    left: 628px;
    top: 148px;
    margin: 0;
    font: 400 48px/1 "Tinos", serif;
    color: var(--flavour-red);
  }
  .weight-bar {
    position: absolute;
    left: 634px;
    top: 199px;
    width: 319px;
    height: 29px;
    background: linear-gradient(90deg, var(--band-red-dark), var(--weight-red) 45%, var(--weight-red) 80%, rgba(179,33,29,0.4));
    color: #fff;
    font: 700 19px/29px "Tinos", serif;
    text-align: center;
  }
  .bag-count {
    position: absolute;
    left: 760px;
    top: 236px;
    margin: 0;
    font: 700 10px/1 "Tinos", serif;
    letter-spacing: 0.5px;
    color: var(--weight-red);
  }
  .fruit-art {
    position: absolute;
    left: 562px;
    top: 256px;
    width: 284px;
    height: 214px;
    background: var(--fruit-orange);
  }

  .brand-name {
    position: absolute;
    left: 872px;
    top: 388px;
    width: 220px;
    margin: 0;
    text-align: center;
    font: 400 32px/1.05 "Tinos", serif;
    color: var(--brand-ink);
  }

  .tagline-band {
    position: absolute;
    left: 0;
    right: 0;
    bottom: 0;
    height: 80px;
    background: linear-gradient(180deg, var(--band-red-dark) 0 8%, var(--band-red) 12% 30%, #5e1215 40%, var(--band-red) 72%, var(--band-red-dark) 100%);
  }
  .tagline {
    position: absolute;
    left: 0;
    right: 0;
    top: 27px;
    margin: 0;
    text-align: center;
    font: 400 24px/1 "Tinos", serif;
    letter-spacing: 1.5px;
    color: var(--band-text);
  }
</style>
</head>
<body>
  <section class="carton-front">
    <div class="leaf-texture leaf-texture--left" role="img" aria-label="Warm yellow leaf-vein texture"></div>
    <div class="leaf-texture leaf-texture--right" role="img" aria-label="Orange and pink leaf-vein texture"></div>

    <h2 class="side-title">Black Tea</h2>
    <p class="side-flavour">Peach Apricot</p>
    <p class="side-copy">Lorem ipsum dolor sit amet, consectetuer adipiscing elit, sed diam nonummy nibh euismod tincidunt ut laoreet dolore magna aliquam erat volutpat.</p>
    <p class="side-disclaimer">*These statements have not been evaluated by the Food &amp; Drug Administration. This product is not intended to diagnose, treat, cure or prevent any disease.</p>
    <p class="distributor">Distributed by<br>Company Name<br>Address, State, Zip</p>

    <div class="tea-window" role="img" aria-label="Green watercolour splash with a leaf-shaped window showing loose black tea leaves"></div>

    <h1 class="product-title">Black Tea</h1>
    <p class="product-flavour">Peach Apricot</p>
    <div class="weight-bar">50 g</div>
    <p class="bag-count">25 TEA BAGS</p>

    <div class="fruit-art" role="img" aria-label="Illustration of a ripe peach and halved apricots with green leaves"></div>

    <p class="brand-name">Calder Tea<br>London</p>

    <div class="tagline-band">
      <p class="tagline">A Fine Speciality Tea</p>
    </div>
  </section>
</body>
</html>
```